Ruvella Sign

Design a sign for Pizza and Pasta restaurant in New Jersey
Black background
Size = 120" w x 23.5" h
Ruvella - top line
Brick Oven Pizza & Pasta - second line

Target Market(s)

everybody

Industry/Entity Type

restaurant

Font styles to use
Decorative
Script

Colors

Designer to choose only greyscale colors for use in the design.

Requirements
Must have
• Brick Oven Pizza & Pasta
Nice to have
• Vector file

```html
<!DOCTYPE html>
<html lang="en">
<head>
<meta charset="utf-8">
<title>Ruvella Sign Concepts</title>
<link rel="stylesheet" href="https://fonts.googleapis.com/css2?family=Work+Sans:ital,wght@0,600;0,700;0,800;1,800&display=swap">
<style>
  :root {
    --stage: #2a2c31;
    --sign-black: #000000;
    --brand-yellow: #f0bb00;
    --text-white: #ffffff;
    --pizza-crust: #c98a4a;
    --pizza-sauce: #b8412a;
    --plate: #1a1a1a;
  }
  * { margin: 0; padding: 0; box-sizing: border-box; }
  html, body { width: 1200px; height: 1200px; overflow: hidden; }
  body {
    background: var(--stage);
    font-family: "Work Sans", Arial, sans-serif;
    position: relative;
  }
  .sign {
    position: absolute;
    width: 1079px;
    height: 211px;
    background: var(--sign-black);
    overflow: hidden;
    box-shadow: 0 10px 24px rgba(0,0,0,0.45);
  }
  .sign--one   { left: 56px; top: 94px; }
  .sign--two   { left: 56px; top: 361px; }
  .sign--three { left: 56px; top: 628px; }
  .sign--four  { left: 60px; top: 895px; }

  .food-photo { position: absolute; left: 0; top: 0; width: 531px; height: 211px; }
  .corner-arc { position: absolute; right: 0; top: 0; width: 1079px; height: 211px; }

  .pizza-photo {
    position: absolute; left: 950px; top: -40px;
    width: 170px; height: 170px; border-radius: 50%;
    background: radial-gradient(circle at 45% 50%, var(--pizza-sauce), var(--pizza-crust) 70%, var(--plate) 74%);
  }

  .wordmark {
    position: absolute;
    color: var(--text-white);
    font-weight: 800;
    line-height: 1;
    white-space: nowrap;
    z-index: 2;
  }
  .tagline {
    position: absolute;
    font-weight: 700;
    line-height: 1;
    white-space: nowrap;
    color: var(--text-white);
    z-index: 2;
  }
  .tagline--accent { color: var(--brand-yellow); }

  .tag-box {
    position: absolute;
    left: 768px; top: 114px;
    width: 279px; height: 64px;
    background: var(--brand-yellow);
    color: var(--sign-black);
    font-weight: 700;
    font-size: 40px;
    line-height: 1;
    display: flex; align-items: center; justify-content: center;
    white-space: nowrap;
    z-index: 3;
  }
  .tag-box--italic {
    font-style: italic; font-weight: 800; font-size: 35px;
    left: 771px; width: 268px; padding-right: 4px;
  }
</style>
</head>
<body>

<section class="sign sign--one">
  <svg class="food-photo" viewBox="0 0 531 211" role="img" aria-label="Photo of pepperoni pizza slices beside spaghetti with shrimp on a dark plate">
    <defs>
      <linearGradient id="pizza1" x1="0" y1="0" x2="1" y2="1">
        <stop offset="0" stop-color="#c98a4a"/><stop offset="0.5" stop-color="#b8412a"/><stop offset="1" stop-color="#d9a066"/>
      </linearGradient>
      <linearGradient id="pasta1" x1="0" y1="0" x2="1" y2="1">
        <stop offset="0" stop-color="#f5b03a"/><stop offset="0.6" stop-color="#e0702c"/><stop offset="1" stop-color="#c9482a"/>
      </linearGradient>
    </defs>
    <rect x="0" y="0" width="258" height="211" fill="url(#pizza1)"/>
    <path d="M261 0 H470 A130 140 0 0 1 531 105 A130 140 0 0 1 470 211 H261 Z" fill="#1a1a1a"/>
    <path d="M261 0 H430 A120 130 0 0 1 490 105 A120 130 0 0 1 430 211 H261 Z" fill="url(#pasta1)"/>
  </svg>
  <svg class="corner-arc" viewBox="0 0 1079 211" aria-hidden="true">
    <path d="M990 0 C990 70 1030 125 1079 141 L1079 0 Z" fill="var(--brand-yellow)"/>
  </svg>
  <div class="wordmark" style="left:564px; top:54px; font-size:69px;">RUVELLA</div>
  <div class="tagline" style="left:564px; top:122px; font-size:36px;"><span class="tagline--accent">Brick Oven</span> Pizza &amp; Pasta</div>
</section>

<section class="sign sign--two">
  <svg class="food-photo" viewBox="0 0 531 211" role="img" aria-label="Photo of pepperoni pizza slices beside spaghetti with shrimp on a dark plate">
    <defs>
      <linearGradient id="pizza2" x1="0" y1="0" x2="1" y2="1">
        <stop offset="0" stop-color="#c98a4a"/><stop offset="0.5" stop-color="#b8412a"/><stop offset="1" stop-color="#d9a066"/>
      </linearGradient>
      <linearGradient id="pasta2" x1="0" y1="0" x2="1" y2="1">
        <stop offset="0" stop-color="#f5b03a"/><stop offset="0.6" stop-color="#e0702c"/><stop offset="1" stop-color="#c9482a"/>
      </linearGradient>
    </defs>
    <rect x="0" y="0" width="258" height="211" fill="url(#pizza2)"/>
    <path d="M261 0 H470 A130 140 0 0 1 531 105 A130 140 0 0 1 470 211 H261 Z" fill="#1a1a1a"/>
    <path d="M261 0 H430 A120 130 0 0 1 490 105 A120 130 0 0 1 430 211 H261 Z" fill="url(#pasta2)"/>
  </svg>
  <div class="wordmark" style="left:553px; top:30px; font-size:82px;">RUVELLA</div>
  <div class="tagline" style="left:553px; top:128px; font-size:38px;">Brick Oven</div>
  <div class="tag-box">Pizza &amp; Pasta</div>
</section>

<section class="sign sign--three">
  <svg class="food-photo" viewBox="0 0 531 211" role="img" aria-label="Photo of pepperoni pizza slices beside spaghetti with shrimp on a dark plate">
    <defs>
      <linearGradient id="pizza3" x1="0" y1="0" x2="1" y2="1">
        <stop offset="0" stop-color="#c98a4a"/><stop offset="0.5" stop-color="#b8412a"/><stop offset="1" stop-color="#d9a066"/>
      </linearGradient>
      <linearGradient id="pasta3" x1="0" y1="0" x2="1" y2="1">
        <stop offset="0" stop-color="#f5b03a"/><stop offset="0.6" stop-color="#e0702c"/><stop offset="1" stop-color="#c9482a"/>
      </linearGradient>
    </defs>
    <rect x="0" y="0" width="258" height="211" fill="url(#pizza3)"/>
    <path d="M261 0 H470 A130 140 0 0 1 531 105 A130 140 0 0 1 470 211 H261 Z" fill="#1a1a1a"/>
    <path d="M261 0 H430 A120 130 0 0 1 490 105 A120 130 0 0 1 430 211 H261 Z" fill="url(#pasta3)"/>
  </svg>
  <div class="pizza-photo" role="img" aria-label="Photo of a whole sliced pizza on a dark pan"></div>
  <div class="wordmark" style="left:553px; top:30px; font-size:82px;">RUVELLA</div>
  <div class="tagline" style="left:553px; top:128px; font-size:38px;">Brick Oven</div>
  <div class="tag-box">Pizza &amp; Pasta</div>
</section>

<section class="sign sign--four">
  <svg class="food-photo" viewBox="0 0 531 211" role="img" aria-label="Photo of pepperoni pizza slices beside spaghetti with shrimp on a dark plate">
    <defs>
      <linearGradient id="pizza4" x1="0" y1="0" x2="1" y2="1">
        <stop offset="0" stop-color="#c98a4a"/><stop offset="0.5" stop-color="#b8412a"/><stop offset="1" stop-color="#d9a066"/>
      </linearGradient>
      <linearGradient id="pasta4" x1="0" y1="0" x2="1" y2="1">
        <stop offset="0" stop-color="#f5b03a"/><stop offset="0.6" stop-color="#e0702c"/><stop offset="1" stop-color="#c9482a"/>
      </linearGradient>
    </defs>
    <rect x="0" y="0" width="258" height="211" fill="url(#pizza4)"/>
    <path d="M261 0 H470 A130 140 0 0 1 531 105 A130 140 0 0 1 470 211 H261 Z" fill="#1a1a1a"/>
    <path d="M261 0 H430 A120 130 0 0 1 490 105 A120 130 0 0 1 430 211 H261 Z" fill="url(#pasta4)"/>
  </svg>
  <div class="wordmark" style="left:565px; top:40px; font-size:69px;">RUVELLA</div>
  <div class="tagline" style="left:566px; top:128px; font-size:37px; font-weight:600;">Brick Oven</div>
  <div class="tag-box tag-box--italic">Pizza &amp; Pasta</div>
</section>

</body>
</html>
```